Billboard for Law Firm

I am looking for a billboard designs. Our branding right now is not good. The logo has to stay the same, but please help come up with something modern, airy, perhaps geometric for the supporting design elements.
Colors should probably be red and blue, or shades of blue, but you can play with the exact shades. Doesn't have to match what you see in the attachment.

The billboard should include:

- Some type of design to bring it to life.

- Logo

- Accident & Injury Law

- 614.300.7000

- Disclaimer (very small text): No Representation Made That The Quality of Legal Services Performed is Greater Than the Those of Other Attorneys

Slogan (very large): Grits, Gravy, and a Good Attorney

______________

Target Market(s)

Southern United States

Industry/Entity Type

Legal Services

Font styles to use
Serif
Sans Serif

Colors
0054AA
0677BA
7BADD7
CADEEF
E8F1F8
EB3D1F
EC4F4E
F09395
F8D3D4
FCEDEE

Requirements
Must have
• Help Make it Memorable and Easy to Read (large text for slogan)
Nice to have
• Some shapes or design elements that may become part of our branding.

```html
<!DOCTYPE html>
<html lang="en">
<head>
<meta charset="utf-8">
<title>The Hartwell Firm – Billboard</title>
<link rel="stylesheet" href="https://fonts.googleapis.com/css2?family=Oswald:wght@200;300;700&family=Cinzel:wght@600&family=Lato:wght@400&display=swap">
<style>
  :root {
    --navy: #030d5c;
    --swoosh: #2c3483;
    --periwinkle: #717dc6;
    --tagline: #7e87c9;
    --white: #ffffff;
    --red: #d11016;
    --fine-print: #a7acd2;
  }
  html, body {
    margin: 0;
    padding: 0;
    overflow: hidden;
    background: var(--navy);
  }
  .billboard {
    position: relative;
    width: 1200px;
    height: 675px;
    overflow: hidden;
    background: var(--navy);
    font-family: "Oswald", sans-serif;
  }
  .swoosh {
    position: absolute;
    inset: 0;
    width: 1200px;
    height: 675px;
  }
  .portrait {
    position: absolute;
    left: 20px;
    top: 34px;
    width: 520px;
    height: 641px;
    border-radius: 200px 200px 0 0;
    background:
      radial-gradient(ellipse 90px 120px at 275px 120px, rgba(214,170,150,0.55), rgba(214,170,150,0) 100%),
      linear-gradient(180deg, rgba(60,80,130,0) 0%, rgba(58,82,130,0.75) 40%, rgba(40,60,115,0.6) 80%, rgba(3,13,92,0) 100%);
  }
  .brand {
    position: absolute;
    right: 45px;
    top: 60px;
    display: flex;
    align-items: center;
    gap: 14px;
    color: var(--white);
  }
  .brand-mark {
    width: 42px;
    height: 42px;
    border-radius: 50%;
    background: var(--red);
  }
  .brand-name {
    font-family: "Cinzel", serif;
    font-weight: 600;
    font-size: 34px;
    line-height: 1;
    letter-spacing: 1px;
  }
  .practice {
    position: absolute;
    right: 45px;
    top: 158px;
    margin: 0;
    font-weight: 300;
    font-size: 24px;
    letter-spacing: 14.5px;
    margin-right: -14px;
    color: var(--tagline);
    line-height: 1;
  }
  .slogan {
    position: absolute;
    right: 45px;
    top: 225px;
    margin: 0;
    text-align: right;
    line-height: 1;
  }
  .slogan-lead {
    display: block;
    font-weight: 200;
    font-size: 120px;
    color: var(--periwinkle);
    letter-spacing: 0.5px;
  }
  .slogan-punch {
    display: block;
    margin-top: -2px;
    font-weight: 700;
    font-size: 140px;
    color: var(--white);
    letter-spacing: -1px;
  }
  .phone {
    position: absolute;
    right: 45px;
    top: 478px;
    margin: 0;
    font-weight: 700;
    font-size: 128px;
    line-height: 1.05;
    color: var(--red);
    letter-spacing: 2px;
  }
  .disclaimer {
    position: absolute;
    right: 45px;
    top: 629px;
    margin: 0;
    font-family: "Lato", sans-serif;
    font-size: 14px;
    color: var(--fine-print);
    line-height: 1;
  }
</style>
</head>
<body>
  <main class="billboard">
    <svg class="swoosh" viewBox="0 0 1200 675" aria-hidden="true">
      <path fill="var(--swoosh)" opacity="0.85"
        d="M470 0 C520 60 480 140 360 175 C200 220 90 260 50 420 C30 500 20 560 0 600 L0 675 L30 675 C60 560 110 420 210 300 C300 200 430 190 500 100 C525 60 515 20 505 0 Z"/>
    </svg>

    <div class="portrait" role="img" aria-label="Smiling attorney in a blue suit and light blue shirt with arms crossed"></div>

    <div class="brand">
      <span class="brand-mark"></span>
      <span class="brand-name">The Hartwell Firm</span>
    </div>
    <p class="practice">ACCIDENT &amp; INJURY LAW</p>

    <h1 class="slogan">
      <span class="slogan-lead">GRITS, GRAVY &amp;</span>
      <span class="slogan-punch">GOOD ATTORNEY</span>
    </h1>

    <p class="phone">(614) 300 7000</p>

    <p class="disclaimer">No Representation Made That The Quality of Legal Service Performed is Greater Than the Those of Other Attorneys</p>
  </main>
</body>
</html>
```